Speisekarten-Design für gehobenes italienisches Restaurant
Zielgruppe
Wir sind ein gehobenes italienisches Restaurant und suchen ein neues Design für unsere Speisekarte. Wir haben ein eher älteres Publikum.
Aufgabenstellung
Wir möchten eine elegantes modernes Design. Einzelseiten im A4 Format.

```html
<!DOCTYPE html>
<html lang="de">
<head>
<meta charset="utf-8">
<title>Villa Serena – Speise- &amp; Getränkekarte</title>
<link rel="stylesheet" href="https://fonts.googleapis.com/css2?family=Allura&family=Crimson+Text:ital,wght@0,400;0,600;0,700;1,700&family=Open+Sans:wght@400;600&display=swap">
<style>
  :root {
    --backdrop: #e8e4de;
    --paper: #d9d1c3;
    --maroon: #7b1a2f;
    --ink: #1e1b18;
    --olive: #3b3a30;
    --green: #0a8a2a;
    --white: #ffffff;
    --red: #e3111b;
    --orange: #e8762a;
  }
  * { margin: 0; padding: 0; box-sizing: border-box; }
  html, body { width: 1200px; height: 765px; overflow: hidden; }
  body { background: var(--backdrop); position: relative; font-family: "Open Sans", sans-serif; color: var(--ink); }

  .page { position: absolute; top: 186px; width: 280px; height: 394px; background: var(--paper); overflow: hidden; box-shadow: 0 1px 3px rgba(0,0,0,.15); }
  .page--cover { left: 12px; }
  .page--hours { left: 313px; }
  .page--welcome { left: 615px; }
  .page--drinks { left: 917px; }

  .abs { position: absolute; }
  .center { left: 0; right: 0; text-align: center; }
  .script { font-family: "Allura", cursive; }
  .serif { font-family: "Crimson Text", serif; }

  .flag { position: absolute; left: 49px; top: 381px; width: 182px; height: 6px; display: flex; }
  .flag span { flex: 1; }
  .flag .g { background: var(--green); } .flag .w { background: var(--white); } .flag .r { background: var(--red); }

  /* cover */
  .cover-greeting { top: 12px; font-size: 30px; line-height: 24px; }
  .brand-name { font-family: "Crimson Text", serif; font-weight: 600; color: var(--maroon); }
  .cover-brand { top: 100px; font-size: 36px; }
  .cover-sub { top: 172px; font-family: "Crimson Text", serif; font-size: 13px; line-height: 17px; }
  .cover-title { top: 282px; font-family: "Crimson Text", serif; font-weight: 600; font-size: 18px; }

  /* inner header */
  .branch { position: absolute; top: 22px; width: 70px; height: 22px; background: linear-gradient(90deg, rgba(59,58,48,0), rgba(59,58,48,.55) 40%, rgba(59,58,48,.55) 60%, rgba(59,58,48,0)); border-radius: 11px; }
  .branch--left { left: 7px; } .branch--right { right: 7px; }
  .header-brand { top: 20px; font-size: 20px; }

  .footer { top: 355px; font-family: "Crimson Text", serif; font-size: 6.5px; line-height: 8.5px; }

  /* hours */
  .hours-title { top: 220px; font-family: "Crimson Text", serif; font-weight: 700; font-size: 9px; }
  .hours-list { top: 243px; font-family: "Crimson Text", serif; font-weight: 700; font-size: 6.5px; line-height: 8.5px; }
  .hours-web { top: 328px; font-family: "Crimson Text", serif; font-weight: 700; font-size: 6.5px; }

  /* welcome */
  .letter-salutation { top: 64px; left: 9px; font-size: 26px; }
  .letter-body { top: 100px; left: 9px; width: 260px; font-size: 6.6px; line-height: 8.4px; }
  .letter-body p { margin-bottom: 8px; }
  .letter-sign { font-size: 14px; line-height: 12px; margin: 2px 0 3px; }
  .letter-fine { top: 325px; left: 9px; width: 262px; font-size: 4.2px; line-height: 5.4px; }

  /* drinks */
  .aperitif-title { top: 60px; left: 70px; width: 140px; text-align: center; font-family: "Crimson Text", serif; font-style: italic; font-weight: 700; font-size: 14px; }
  .aperitif { left: 70px; width: 140px; text-align: center; }
  .aperitif .name { font-size: 6.8px; }
  .aperitif .sub { font-size: 4px; font-weight: 600; }
  .drink-photo { top: 60px; left: 207px; width: 60px; height: 88px; border-radius: 30px 30px 10px 10px; background: radial-gradient(circle at 50% 40%, var(--orange), rgba(232,118,42,.35) 60%, rgba(232,118,42,0) 75%); }
  .section-head { font-size: 15px; }
  .item { position: absolute; width: 120px; }
  .item--left { left: 7px; }
  .item--right { right: 7px; text-align: right; }
  .item .name { font-size: 6.8px; line-height: 8px; }
  .item .desc { font-size: 4px; line-height: 5px; font-weight: 600; }
</style>
</head>
<body>

<section class="page page--cover">
  <div class="abs center script cover-greeting">Herzlich<br>Willkommen</div>
  <div class="abs center brand-name cover-brand">Villa Serena</div>
  <div class="abs center cover-sub">Ristorante-Pizzeria<br>Villa-Serena</div>
  <div class="abs center cover-title">Speise- &amp; Getränkekarte</div>
  <div class="flag"><span class="g"></span><span class="w"></span><span class="r"></span></div>
</section>

<section class="page page--hours">
  <div class="branch branch--left" role="img" aria-label="Olivenzweig-Ornament"></div>
  <div class="abs center brand-name header-brand">Villa Serena</div>
  <div class="branch branch--right" role="img" aria-label="Olivenzweig-Ornament"></div>
  <div class="abs center hours-title">Öffnungszeiten</div>
  <div class="abs center hours-list">
    Montag – Freitag<br>
    11:30 Uhr bis 14:30 Uhr und 17:00 Uhr bis 23:00 Uhr<br>
    Samstag<br>
    11:30 Uhr bis 14:30 Uhr und 17:00 Uhr bis 24:00 Uhr<br>
    Sonn- und Feiertage<br>
    durchgehend von 11:00 Uhr bis 21:30 Uhr<br>
    Warme Küche mittags 14:00 Uhr<br>
    Bestellschluss, Mo-Sa abends um 22:30 Uhr, So um 21:00 Uhr
  </div>
  <div class="abs center hours-web">www.villa-serena-ristorante.de</div>
  <div class="abs center footer">Ristorante-Pizzeria Villa-Serena<br>Lindenallee 14, 63500 Seestadt-Nord<br>Tel: 06100 - 12 345 67</div>
  <div class="flag"><span class="g"></span><span class="w"></span><span class="r"></span></div>
</section>

<section class="page page--welcome">
  <div class="branch branch--left" role="img" aria-label="Olivenzweig-Ornament"></div>
  <div class="abs center brand-name header-brand">Villa Serena</div>
  <div class="branch branch--right" role="img" aria-label="Olivenzweig-Ornament"></div>
  <div class="abs script letter-salutation">Liebe Gäste,</div>
  <div class="abs letter-body">
    <p>es ist uns eine Freude, Sie als Gäste im Ristorante Villa Serena in Seestadt begrüßen zu können!</p>
    <p>Wir wünschen Ihnen neben einem angenehmen Aufenthalt natürlich insbesondere einen ‚Guten Appetit‘. Genießen Sie mediterrane Spezialitäten, italienische Küche und Leckeres aus deutschen Landen.</p>
    <p>Ob in unserem Haus (separierbare Räumlichkeiten, Platz für bis zu 100 Gäste) oder auf unserer großzügigen Terrasse (Platz für bis 120 Gäste) … genießen Sie italienische Lebensfreude und echte Gastfreundschaft!</p>
    <p>Und anlässlich einer Feier sind wir natürlich ebenfalls Ihr<br>kompetenter Ansprechpartner.</p>
    <p>Falls Sie Fragen zu unseren Gerichten haben oder einen besonderen Wunsch äußern möchten – scheuen Sie sich nicht, uns zu informieren. Wir werden –wenn denn irgend möglich– versuchen, Ihren Wunsch zu erfüllen.</p>
    <p>Lassen Sie sich verwöhnen und genießen Sie<br>Ihren Aufenthalt im Villa Serena</p>
    <div>Ihre</div>
    <div class="script letter-sign">Marco und Luca</div>
    <div>und das gesamte Villa Serena-Team</div>
  </div>
  <div class="abs letter-fine">Alle angegebenen Preise sind in Euro angegeben und beinhalten die gesetzlich vorgeschriebene Mehrwertsteuer in Höhe des jeweils zutreffenden Steuersatzes.<br>Inhalts- und Zusatzstoffe sind mit ZIFFERN gekennzeichnet, Allergene in LETTERN. Erläuterungen hierzu am Ende dieser Speisekarte</div>
  <div class="abs center footer">Ristorante-Pizzeria Villa-Serena<br>Lindenallee 14, 63500 Seestadt-Nord<br>Tel: 06100 - 12 345 67</div>
  <div class="flag"><span class="g"></span><span class="w"></span><span class="r"></span></div>
</section>

<section class="page page--drinks">
  <div class="branch branch--left" role="img" aria-label="Olivenzweig-Ornament"></div>
  <div class="abs center brand-name header-brand">Villa Serena</div>
  <div class="branch branch--right" role="img" aria-label="Olivenzweig-Ornament"></div>

  <div class="abs aperitif-title">Aperitifs</div>
  <div class="abs aperitif" style="top:87px"><div class="name">Sherry</div><div class="sub">trocken | medium | süß &nbsp;5cl &nbsp;&nbsp;5.90</div></div>
  <div class="abs aperitif" style="top:108px"><div class="name">Vermouth</div><div class="sub">bianco | rosso &nbsp;5cl &nbsp;&nbsp;6.00</div></div>
  <div class="abs aperitif" style="top:129px"><div class="name">Bitter Rosso</div><div class="sub">bianco | rosso &nbsp;5cl &nbsp;&nbsp;6.00</div></div>
  <div class="abs drink-photo" role="img" aria-label="Foto: zwei Spritz-Gläser mit Orangenscheiben"></div>

  <div class="abs script section-head" style="top:150px;left:8px">Spritziges</div>
  <div class="abs script section-head" style="top:150px;right:8px">Klassiker</div>
  <div class="abs script section-head" style="top:255px;right:8px">Alkoholfrei</div>

  <div class="item item--left" style="top:176px"><div class="name">Hugo</div><div class="desc">Prosecco Spumante, Holunderblütensirup, Soda,<br>Pfefferminz &nbsp;0,2 &nbsp;7.90</div></div>
  <div class="item item--left" style="top:202px"><div class="name">Black Hugo</div><div class="desc">Prosecco Spumante, Holunderblütensirup, Soda,<br>Pfefferminz &nbsp;0,2 &nbsp;7.90</div></div>
  <div class="item item--left" style="top:228px"><div class="name">Arancio Spritz</div><div class="desc">Prosecco Spumante, Arancio Bitter, Soda<br>Orangenscheibe &nbsp;0,2 &nbsp;7.90</div></div>
  <div class="item item--left" style="top:254px"><div class="name">Limoncello Spritz</div><div class="desc">Prosecco Spumante, Limoncello, Soda,<br>Zitrone &nbsp;0,2 &nbsp;7.90</div></div>
  <div class="item item--left" style="top:280px"><div class="name">Rosé Wild Berry</div><div class="desc">Rosé Aperitif, Prosecco Spumante, Wild Berry Tonic,<br>Beeren, Pfefferminz &nbsp;0,2 &nbsp;8.90</div></div>
  <div class="item item--left" style="top:306px"><div class="name">Lavendel Spritz</div><div class="desc">Lavendelsirup, Prosecco Spumante, Soda,<br>Zitrone &nbsp;0,2 &nbsp;8.90</div></div>
  <div class="item item--left" style="top:332px"><div class="name">Moscow Mule</div><div class="desc">Vodka, Limettensaft, Ginger Beer,<br>Ingwer, Pfefferminz &nbsp;0,2 &nbsp;8.90</div></div>

  <div class="item item--right" style="top:176px"><div class="name">Espresso Martini</div><div class="desc">Espresso Shot, Vodka,<br>Kaffeelikör, Sahnelikör &nbsp;10.90</div></div>
  <div class="item item--right" style="top:202px"><div class="name">Negroni</div><div class="desc">Bitter Rosso, Gin, Vermouth Rosso,<br>Orangenscheibe &nbsp;9.90</div></div>
  <div class="item item--right" style="top:228px"><div class="name">Grand Ginger</div><div class="desc">Orangenlikör, Ginger Ale, Limettensaft,<br>Orangenscheibe &nbsp;0,2 &nbsp;9.90</div></div>
  <div class="item item--right" style="top:280px"><div class="name">Hugo alkoholfrei</div><div class="desc">Ginger Ale, Holundersirup, Limette, Pfefferminz<br>0,2 &nbsp;7.50</div></div>
  <div class="item item--right" style="top:306px"><div class="name">Black Hugo alkoholfrei</div><div class="desc">Holundersirup, Johannisbeersaft<br>0,2 &nbsp;7.50</div></div>
  <div class="item item--right" style="top:332px"><div class="name">Wild Berry alkoholfrei</div><div class="desc">Wild Berry Tonic, Mineralwasser, Beeren<br>Pfefferminz &nbsp;0,2 &nbsp;7.90</div></div>

  <div class="abs center footer">Ristorante-Pizzeria Villa-Serena<br>Lindenallee 14, 63500 Seestadt-Nord<br>Tel: 06100 - 12 345 67</div>
  <div class="flag"><span class="g"></span><span class="w"></span><span class="r"></span></div>
</section>

</body>
</html>
```